Stationary & Business Card design for Solo Law Firm
stationary and business card design
Stationary & Business Card design for Solo Law Firm - Law
Creative Brief
Professional
Mira Dalton
Attorney at Law
317 W. Halverd Street, Suite 508 Colorado Springs, CO 80903
miradalton@kestrelpointlegal.example
kestrelpointlegal.example
underneath my logo I want the following to appear Family Law - Business - Trust & Estates (the spacing or symbol between these terms is up to you)
Logo on the back with the wording above underneath
quillmarsh quillmarsh
#98 can you make the text on the front vertical? and use the back from your #95 with the blue background. I like your submission #72 as well.
#134 can you make the text on the front go vertically instead of horizontally? also can you make the scales on the back bigger?
#141 on the front can you make it vertical? and on the back can you make the logo bigger and put the scales on the back?

```html
<!DOCTYPE html>
<html lang="en">
<head>
<meta charset="utf-8">
<title>Kestrel Point Legal — Business Card</title>
<link rel="stylesheet" href="https://fonts.googleapis.com/css2?family=Cinzel:wght@400;600&family=Cormorant+Garamond:wght@400;500&display=swap">
<style>
  :root {
    --backdrop: #e9e9e9;
    --card-white: #ffffff;
    --copper: #c0603e;
    --copper-deep: #a9502f;
    --navy: #2c4a9c;
    --ink: #3a3a3a;
    --cream: #fbefe8;
  }
  * { margin: 0; padding: 0; box-sizing: border-box; }
  html, body { width: 1200px; height: 908px; overflow: hidden; }
  body {
    background: var(--backdrop);
    display: flex;
    align-items: center;
    justify-content: center;
    gap: 40px;
    font-family: "Cormorant Garamond", serif;
  }
  .card {
    width: 540px;
    height: 309px;
    border-radius: 26px;
    box-shadow: 0 6px 18px rgba(0,0,0,0.18);
    position: relative;
    overflow: hidden;
  }
  /* Front */
  .card--front {
    background: linear-gradient(135deg, var(--copper) 0%, var(--copper-deep) 100%);
    color: var(--cream);
    display: flex;
    flex-direction: column;
    align-items: center;
    justify-content: center;
    gap: 20px;
  }
  .firm-name {
    font-family: "Cinzel", serif;
    font-weight: 400;
    font-size: 38px;
    letter-spacing: 1px;
    line-height: 1;
  }
  .card--front .firm-name { color: var(--cream); }
  .practice-areas {
    font-family: "Cinzel", serif;
    font-size: 15px;
    letter-spacing: 1.5px;
  }
  /* Back */
  .card--back {
    background: var(--card-white);
    display: flex;
    padding: 48px 30px 40px 36px;
    gap: 20px;
  }
  .identity {
    flex: 1;
    min-width: 0;
    display: flex;
    flex-direction: column;
    justify-content: space-between;
  }
  .card--back .firm-name {
    color: var(--copper);
    font-size: 24px;
    line-height: 1.1;
    padding-bottom: 12px;
    border-bottom: 1.5px solid var(--navy);
    margin-top: 34px;
  }
  .person-name {
    font-family: "Cinzel", serif;
    color: var(--navy);
    font-size: 19px;
    letter-spacing: 1px;
  }
  .person-title {
    font-family: "Cinzel", serif;
    color: var(--copper);
    font-size: 14px;
    letter-spacing: 1px;
    margin-top: 2px;
  }
  .contact {
    flex: none;
    width: 238px;
    color: var(--ink);
    font-size: 12.5px;
    line-height: 1.4;
  }
  .address { margin-bottom: 10px; white-space: nowrap; }
  .contact-line {
    display: flex;
    align-items: center;
    gap: 6px;
    white-space: nowrap;
  }
  .contact-line svg { flex: none; width: 11px; height: 11px; fill: var(--copper); }
</style>
</head>
<body>
  <section class="card card--front" aria-label="Card front">
    <div class="firm-name">Kestrel Point Legal</div>
    <div class="practice-areas">Family Law · Business · Trust &amp; Estates</div>
  </section>

  <section class="card card--back" aria-label="Card back">
    <div class="identity">
      <div class="firm-name">Kestrel Point Legal</div>
      <div>
        <div class="person-name">Mira Dalton</div>
        <div class="person-title">Attorney at Law</div>
      </div>
    </div>
    <div class="contact">
      <div class="address">317 W. Halverd Street, Suite 508<br>Colorado Springs, CO 80903</div>
      <div class="contact-line">
        <svg viewBox="0 0 12 12"><path d="M2.5 1h2l1 2.5-1.3 1a6 6 0 0 0 3.3 3.3l1-1.3L11 7.5v2a1 1 0 0 1-1 1A9 9 0 0 1 1.5 2a1 1 0 0 1 1-1z"/></svg>
        (719) 555-0142
      </div>
      <div class="contact-line">
        <svg viewBox="0 0 12 12"><path d="M1 2.5h10v7H1z M1.5 3l4.5 3.5L10.5 3" stroke="#fff" stroke-width="0.8"/></svg>
        miradalton@kestrelpointlegal.example
      </div>
      <div class="contact-line">
        <svg viewBox="0 0 12 12"><circle cx="6" cy="6" r="5"/></svg>
        kestrelpointlegal.example
      </div>
      <div class="contact-line">
        <svg viewBox="0 0 12 12"><rect x="1" y="1" width="10" height="10" rx="2"/></svg>
        quillmarsh
      </div>
    </div>
  </section>
</body>
</html>
```